Free Charity Events from KOVAPLAY

The purpose of the landing page is to get all visitors excited about playing in our Free $500 Charity Tournaments. The visitors who click on the landing page will receive 3 free entries into 3 different $500 Charity Tournaments. A $500 Blackjack Tournament, a $500 Texas Holdem Tournament, and a $500 Baccarat Tournament.

We also offer Free Qualifying games 24/7, where players can earn additional entries into our real paying tournaments.

We will reward the winners in each tournament with a share of the $500 and we will reward a worthy cause or charity with $500 as well.

The money comes from advertising shown during the qualifying game.

Our website is currently being developed on our teams development server. Here is a private link to the site. https://dev.kovaplay.net Attached are vector images of our logo.

Also attached are two attempts we made at a landing page.

Target Market(s)

Social Game Players

Industry/Entity Type

Games

Contact Information for Business Card

The purpose of the business card will be to promote our Free Charity Games. There will be a code hand written on the card. (Meaning we will need a white box to write the code in) If the holder of the card enters that code during registration, they will receive 3 free entries into our real cash tournaments. The giver of the card will receive the affiliate bonus for referring a new player.

Font styles to use
Serif
Sans Serif

Colors
9bcb3c
0292cd
ec1f27

Requirements
Must have
• Excitement, i also like humor but that isn't a must, excitement is.
Nice to have
• Humor
Should not have
• Too many words, we are looking for that image that says at least a few hundred words.

```html
<!DOCTYPE html>
<html lang="en">
<head>
<meta charset="utf-8">
<title>KOVAPLAY – Free $500 Tournaments</title>
<link rel="stylesheet" href="https://fonts.googleapis.com/css2?family=Barlow:wght@600;700;800&display=swap">
<style>
  :root {
    --green: #7fad3a;
    --green-light: #9bcb3c;
    --blue: #2f6fae;
    --blue-light: #0292cd;
    --red: #d4101f;
    --red-light: #ec1f27;
    --white: #ffffff;
    --ink: #1f2a33;
    --photo-a: #6f8a5c;
    --photo-b: #a29079;
    --photo-c: #4e5d57;
  }
  * { margin: 0; padding: 0; box-sizing: border-box; }
  html, body { width: 1200px; height: 844px; overflow: hidden; background: var(--white); }
  body { font-family: "Barlow", Arial, sans-serif; }

  .landing { position: relative; width: 1200px; height: 844px; overflow: hidden; background: var(--white); }

  .hero-photo {
    position: absolute; inset: 0 0 90px 0;
    background:
      radial-gradient(ellipse 420px 520px at 880px 380px, #b49a82 0%, rgba(180,154,130,0) 70%),
      radial-gradient(ellipse 500px 400px at 200px 200px, #9fae86 0%, rgba(159,174,134,0) 75%),
      linear-gradient(160deg, var(--photo-a) 0%, var(--photo-b) 55%, var(--photo-c) 100%);
  }
  .hero-shade {
    position: absolute; inset: 0 0 90px 0;
    background: linear-gradient(90deg, rgba(40,70,60,0.35) 0%, rgba(40,70,60,0.1) 60%, rgba(0,0,0,0) 100%);
  }
  .hero-curve { position: absolute; left: 0; top: 640px; width: 1200px; height: 204px; }

  .brand {
    position: absolute; left: 173px; top: 40px;
    display: flex; align-items: center; gap: 12px;
  }
  .brand-dot { width: 58px; height: 58px; border-radius: 50%; background: var(--green-light); }
  .brand-name { font-weight: 800; font-size: 56px; line-height: 1; color: var(--blue); letter-spacing: 1px; }

  .headline {
    position: absolute; left: 174px; top: 183px;
    color: var(--white); font-weight: 700; font-size: 46px; line-height: 60px;
    text-shadow: 0 1px 3px rgba(0,0,0,0.25);
  }

  .actions { position: absolute; left: 172px; top: 458px; display: flex; gap: 11px; }
  .btn {
    display: inline-flex; align-items: center; justify-content: center;
    height: 45px; padding: 0 23px; border-radius: 14px 0 14px 0;
    color: var(--white); font-weight: 700; font-size: 16px; text-decoration: none;
  }
  .btn-install { background: var(--green); width: 177px; }
  .btn-learn { background: var(--red); width: 131px; }

  .tournament {
    position: absolute; width: 228px; height: 228px; border-radius: 50%;
    border: 6px solid var(--white);
    display: flex; align-items: center; justify-content: center; text-align: center;
    color: var(--white); font-weight: 700; font-size: 28px; line-height: 32px;
    box-shadow: 0 2px 6px rgba(0,0,0,0.15);
  }
  .tournament-blackjack { left: 238px; top: 582px; background: radial-gradient(circle at 50% 40%, var(--green-light), var(--green) 80%); }
  .tournament-holdem { left: 486px; top: 550px; background: radial-gradient(circle at 50% 40%, #3d86c6, var(--blue) 80%); }
  .tournament-baccarat { left: 741px; top: 582px; background: radial-gradient(circle at 50% 40%, var(--red-light), var(--red) 80%); }

  .page-code { position: absolute; left: 1137px; top: 784px; font-weight: 700; font-size: 14px; color: var(--ink); }
</style>
</head>
<body>
<main class="landing">
  <div class="hero-photo" role="img" aria-label="Smiling young woman at a café table looking at her smartphone"></div>
  <div class="hero-shade"></div>
  <svg class="hero-curve" viewBox="0 0 1200 204" preserveAspectRatio="none" aria-hidden="true">
    <path d="M0 88 Q600 -20 1200 88 L1200 204 L0 204 Z" fill="#ffffff"/>
  </svg>

  <div class="brand">
    <span class="brand-dot"></span>
    <span class="brand-name">KOVAPLAY</span>
  </div>

  <h1 class="headline">
    Qualifying for our<br>
    $500 Tournaments<br>
    Anytime Anywhere<br>
    Completely FREE
  </h1>

  <nav class="actions">
    <a class="btn btn-install" href="https://dev.kovaplay.net">INSTALL THE APP</a>
    <a class="btn btn-learn" href="https://dev.kovaplay.net">LEARN MORE</a>
  </nav>

  <div class="tournament tournament-blackjack">A $500<br>Blackjack<br>Tournament</div>
  <div class="tournament tournament-holdem">A $500<br>Texas Holdem<br>Tournament</div>
  <div class="tournament tournament-baccarat">A $500<br>Baccarat<br>Tournament</div>

  <div class="page-code">C4</div>
</main>
</body>
</html>
```